New business card for a regional office of a US M&A company

We need business card for a finance company, office based in Hong Kong , our Head office is in US, our business is to Merge and acquires companies , the new office will be a regional office for the Asia Pacific region. We want to use the head office logo as attached ( but don't have to be exactly the same, can be a variation to it) as a base and then add Asia Pacific alongside the logo.
We would prefer to have be bilingual Eng + Chinese, although we don't really have Chinese company name .

Industry/Entity Type

Business

Contact Information for Business Card

Carla Beth Soren
 

VP,
APAC M&A Operations
Tovar Crest Asia Pacific Limited
 
Unit 1407, K82
27 Sai Lok Fung Road, 
Hong Kong 
 
M: +852 6481 2037
T : +852 2736 4100
F : +852 2736 4155
VOIP: 4813
 
cbsoren@tovarcrest.com

Font styles to use
Serif
Sans Serif

Colors

Designer to choose colors to be used in the design.

Requirements
Must have
• APAC Office

```html
<!DOCTYPE html>
<html lang="en">
<head>
<meta charset="utf-8">
<title>Tovar Crest Asia Pacific – Business Card</title>
<link rel="stylesheet" href="https://fonts.googleapis.com/css2?family=Open+Sans:wght@700&family=Roboto:wght@300;400;500&display=swap">
<style>
  :root {
    --brand: #12acd2;
    --brand-mid: #5dbdd9;
    --brand-light: #93d2e4;
    --paper: #ffffff;
    --backdrop: #eef1f3;
    --edge: #9aa3a8;
  }
  * { box-sizing: border-box; margin: 0; padding: 0; }
  html, body {
    width: 1200px; height: 650px; overflow: hidden;
    background: var(--backdrop);
    font-family: "Roboto", Arial, sans-serif;
  }
  .sheet {
    width: 1200px; height: 650px;
    display: flex; align-items: center; justify-content: center; gap: 30px;
  }
  .card {
    position: relative; width: 555px; height: 347px;
    background: var(--paper);
    border: 1px solid var(--edge);
    overflow: hidden;
  }
  .card__shapes { position: absolute; inset: 0; width: 100%; height: 100%; }

  /* Wordmark */
  .wordmark { position: absolute; width: max-content; color: var(--brand); }
  .wordmark__badge { display: block; margin: 0 auto; background: var(--brand); }
  .wordmark__name {
    font-family: "Open Sans", Arial, sans-serif; font-weight: 700;
    letter-spacing: 0.5px; white-space: nowrap; line-height: 1;
  }
  .wordmark__region { font-weight: 300; line-height: 1.1; text-align: right; }

  .card--front .wordmark { left: 50%; top: 72px; transform: translateX(-50%); }
  .card--front .wordmark__badge { width: 64px; height: 64px; margin-bottom: 52px; }
  .card--front .wordmark__name { font-size: 47px; }
  .card--front .wordmark__region { font-size: 27px; margin-top: 2px; }

  .card--back .wordmark { left: 31px; top: 72px; }
  .card--back .wordmark__badge { width: 42px; height: 42px; margin-bottom: 22px; }
  .card--back .wordmark__name { font-size: 27px; }
  .card--back .wordmark__region { font-size: 16px; margin-top: 1px; }

  .office-tab {
    position: absolute; left: 0; top: 185px;
    width: 152px; height: 31px; padding-left: 32px;
    background: var(--brand); color: var(--paper);
    font-size: 17px; font-weight: 400; line-height: 31px;
    clip-path: polygon(0 0, 145px 0, 152px 100%, 0 100%);
  }

  /* Contact block */
  .holder { position: absolute; right: 45px; top: 32px; text-align: right; color: var(--paper); }
  .holder__name { font-size: 22px; font-weight: 500; line-height: 1.2; }
  .holder__role { font-size: 11px; font-weight: 400; margin-top: 4px; }
  .holder__dept, .holder__company { font-size: 10px; font-weight: 300; line-height: 1.25; }

  .contacts { position: absolute; left: 315px; top: 114px; list-style: none; color: var(--paper); }
  .contacts__item { display: flex; align-items: flex-start; gap: 16px; font-size: 14px; font-weight: 300; line-height: 17px; margin-bottom: 11px; }
  .contacts__icon { flex: none; width: 18px; height: 18px; }
</style>
</head>
<body>
<main class="sheet">

  <section class="card card--front" aria-label="Card front">
    <svg class="card__shapes" viewBox="0 0 555 347" aria-hidden="true">
      <path d="M75 18 C15 120 35 270 120 347 L180 347 C80 270 42 140 75 18 Z" fill="var(--brand-mid)"/>
      <path d="M75 18 C50 140 85 270 180 347 L148 347 C72 270 52 140 75 18 Z" fill="var(--brand-light)"/>
      <path d="M385 0 L440 0 C500 90 505 210 480 297 C475 200 450 90 385 0 Z" fill="var(--brand-light)"/>
      <path d="M440 0 L470 0 C540 90 530 220 480 297 C505 210 500 90 440 0 Z" fill="var(--brand-mid)"/>
    </svg>
    <div class="wordmark">
      <span class="wordmark__badge" aria-hidden="true"></span>
      <div class="wordmark__name">TOVAR CREST</div>
      <div class="wordmark__region">Asia Pacific</div>
    </div>
  </section>

  <section class="card card--back" aria-label="Card back">
    <svg class="card__shapes" viewBox="0 0 555 347" aria-hidden="true">
      <path d="M285 0 C235 110 235 240 270 347 L555 347 L555 0 Z" fill="var(--brand-mid)"/>
      <path d="M302 0 C255 110 258 240 288 347 L555 347 L555 0 Z" fill="var(--brand)"/>
    </svg>

    <div class="wordmark">
      <span class="wordmark__badge" aria-hidden="true"></span>
      <div class="wordmark__name">TOVAR CREST</div>
      <div class="wordmark__region">Asia Pacific</div>
    </div>
    <div class="office-tab">APAC Office</div>

    <div class="holder">
      <div class="holder__name">Carla Beth Soren</div>
      <div class="holder__role">Vice President</div>
      <div class="holder__dept">APAC M&amp;A Operations</div>
      <div class="holder__company">Tovar Crest Asia Pacific Limited</div>
    </div>

    <ul class="contacts">
      <li class="contacts__item">
        <svg class="contacts__icon" viewBox="0 0 18 18" aria-label="Mobile"><circle cx="9" cy="9" r="8" fill="none" stroke="#fff" stroke-width="1.2"/><path d="M6 5 L7.5 5 L8.2 7 L7.2 7.8 C7.7 9 8.6 9.9 9.8 10.5 L10.6 9.6 L12.6 10.3 L12.6 11.8 C9 12.2 5.6 8.8 6 5 Z" fill="#fff"/></svg>
        <span>+852 6481 2037</span>
      </li>
      <li class="contacts__item">
        <svg class="contacts__icon" viewBox="0 0 18 18" aria-label="Telephone"><circle cx="9" cy="9" r="8" fill="none" stroke="#fff" stroke-width="1.2"/><path d="M5 7 C7 5 11 5 13 7 L12 8 L10.5 7.5 L10.5 6.8 C9.5 6.5 8.5 6.5 7.5 6.8 L7.5 7.5 L6 8 Z M6.5 9 H11.5 L12.5 12.5 H5.5 Z" fill="#fff"/></svg>
        <span>+852 2736 4100</span>
      </li>
      <li class="contacts__item">
        <svg class="contacts__icon" viewBox="0 0 18 18" aria-label="Fax"><circle cx="9" cy="9" r="8" fill="none" stroke="#fff" stroke-width="1.2"/><path d="M6 5 H10 L12 7 V13 H6 Z" fill="none" stroke="#fff" stroke-width="1.1"/><path d="M7.5 9 H10.5 M7.5 11 H10.5" stroke="#fff" stroke-width="1"/></svg>
        <span>+852 2736 4155</span>
      </li>
      <li class="contacts__item">
        <svg class="contacts__icon" viewBox="0 0 18 18" aria-label="VOIP"><circle cx="9" cy="9" r="8" fill="none" stroke="#fff" stroke-width="1.2"/><path d="M6 5 L7.5 5 L8.2 7 L7.2 7.8 C7.7 9 8.6 9.9 9.8 10.5 L10.6 9.6 L12.6 10.3 L12.6 11.8 C9 12.2 5.6 8.8 6 5 Z" fill="#fff"/><path d="M10 4.8 A3.2 3.2 0 0 1 13.2 8" fill="none" stroke="#fff" stroke-width="1"/></svg>
        <span>VOIP: 4813</span>
      </li>
      <li class="contacts__item">
        <svg class="contacts__icon" viewBox="0 0 18 18" aria-label="Email"><circle cx="9" cy="9" r="8" fill="none" stroke="#fff" stroke-width="1.2"/><rect x="5" y="6" width="8" height="6" fill="none" stroke="#fff" stroke-width="1.1"/><path d="M5 6 L9 9.5 L13 6" fill="none" stroke="#fff" stroke-width="1.1"/></svg>
        <span>cbsoren@tovarcrest.com</span>
      </li>
      <li class="contacts__item">
        <svg class="contacts__icon" viewBox="0 0 18 18" aria-label="Address"><circle cx="9" cy="9" r="8" fill="none" stroke="#fff" stroke-width="1.2"/><path d="M9 4.5 L13.5 8.5 H12 V13 H10 V10.5 H8 V13 H6 V8.5 H4.5 Z" fill="#fff"/></svg>
        <span>Unit 1407, K82<br>27 Sai Lok Fung Road,<br>Hong Kong</span>
      </li>
    </ul>
  </section>

</main>
</body>
</html>
```